Pool Services Flyer promote regular pool services

We need a flyer design to be send out as a DL Postcard

We are a pool and spa maintenance business and would like to promote of regular pool services.
Please see our website www.brightripplepoolcare.com.au and our facebook page https://www.facebook.com/pages/Bright-Ripple-Pool-Care/583920174630518

We are pretty flexible with layouts etc Our monthly pool service is $67.00 plus chemicals so we would like this highlighted on our ad. We also so one off, weekly and fortnightly services as well.

We would like our details and logo on front and website also listed.

Target Market(s)

Pool owners

Industry/Entity Type

Pool Service

Colors
33a6d7
0292cd
0555a3
3276b5
85abd2

Requirements
Must have
• Logo
• website address
• phone number
• Price
• Promote the fact that customer wont have to worry about their pool
Nice to have
• like to have a blue wave down the bottom of flyer witht eh contact information in it. Would like to to be crisp not over crowed with information

```html
<!DOCTYPE html>
<html lang="en">
<head>
<meta charset="utf-8">
<title>Bright Ripple Pool Care – Pool Services Flyer</title>
<link rel="stylesheet" href="https://fonts.googleapis.com/css2?family=Questrial&family=Roboto+Condensed:wght@400;700&display=swap">
<style>
  :root{
    --sky:#33a6d7;
    --azure:#0292cd;
    --navy:#0555a3;
    --mid-blue:#3276b5;
    --pale-blue:#85abd2;
    --band-light:#bfe3f6;
    --deep:#0a3f8f;
    --badge-green:#1aa36a;
    --badge-green-dark:#0c7d4f;
    --ring:#d7dbde;
    --teal:#5fc3a6;
    --ink:#111111;
    --white:#ffffff;
  }
  *{margin:0;padding:0;box-sizing:border-box}
  html,body{width:1200px;height:2517px;overflow:hidden;background:var(--white)}
  .flyer{position:relative;width:1200px;height:2517px;overflow:hidden;font-family:"Questrial",sans-serif;color:var(--white)}

  .top-rule{position:absolute;left:0;top:0;width:1200px;height:16px;background:var(--azure)}
  .pool-photo{position:absolute;left:0;top:16px;width:1200px;height:820px;
    background:
      radial-gradient(ellipse 620px 260px at 760px 360px,#2fb6e8 0%,#1a8fd0 55%,transparent 72%),
      linear-gradient(180deg,#8a8680 0%,#a7a29a 40%,#8f8a84 100%)}
  .headline{position:absolute;right:77px;top:296px;text-align:right;font-weight:400;font-size:70px;line-height:84px;color:var(--white)}
  .reassure{position:absolute;right:77px;top:580px;text-align:right;font-size:40px;line-height:50px;color:var(--white)}

  .water{position:absolute;left:0;top:820px;width:1200px;height:764px;
    background:linear-gradient(180deg,#2f8fdc 0%,#1669c4 45%,var(--navy) 100%)}
  .wave{position:absolute;left:0;top:760px;width:1200px;height:240px}
  .droplets{position:absolute;left:440px;top:920px;width:320px;height:150px;border-radius:50%;
    background:radial-gradient(ellipse at center,rgba(255,255,255,.28),rgba(255,255,255,0) 70%)}

  .services{position:absolute;left:80px;top:1066px;list-style:none;font-size:54px;line-height:81px;color:var(--white);white-space:nowrap}

  .offer-band{position:absolute;left:0;top:1584px;width:1200px;height:191px;
    background:linear-gradient(180deg,#d9f0fb 0%,var(--band-light) 100%)}
  .contact-panel{position:absolute;left:0;top:1775px;width:1200px;height:365px;
    background:linear-gradient(180deg,var(--mid-blue) 0%,var(--navy) 60%,var(--deep) 100%)}
  .frequency{position:absolute;left:440px;width:720px;top:1600px;text-align:center;white-space:nowrap;
    font-family:"Roboto Condensed",sans-serif;font-weight:700;font-size:54px;line-height:80px;color:var(--navy)}

  .price-badge{position:absolute;left:42px;top:1525px;width:390px;height:390px;border-radius:50%;
    background:radial-gradient(circle at 40% 30%,#ffffff 0%,var(--ring) 60%,#aeb4b8 100%);
    box-shadow:0 14px 22px rgba(0,0,0,.25)}
  .price-badge__inner{position:absolute;left:24px;top:24px;width:342px;height:342px;border-radius:50%;
    background:radial-gradient(circle at 45% 35%,#22b679 0%,var(--badge-green) 55%,var(--badge-green-dark) 100%);
    display:flex;flex-direction:column;align-items:center;justify-content:center;
    font-family:"Roboto Condensed",sans-serif;color:var(--white);text-align:center;white-space:nowrap}
  .price-badge__label{font-weight:700;font-size:49px;line-height:56px}
  .price-badge__sub{font-size:50px;line-height:60px}
  .price-badge__amount{font-weight:700;font-size:100px;line-height:100px}
  .price-badge__note{font-size:41px;line-height:48px}

  .call-to-action{position:absolute;left:440px;width:700px;top:1812px;text-align:center;font-size:46px;line-height:67px;white-space:nowrap}
  .phones{position:absolute;left:407px;width:780px;top:1948px;text-align:center;font-size:64px;line-height:86px;white-space:nowrap}
  .phones .sep{padding:0 30px}

  .footer-rule{position:absolute;left:0;top:2140px;width:1200px;height:22px;
    background:linear-gradient(180deg,var(--pale-blue) 0 6px,var(--white) 6px 10px,var(--teal) 10px 22px)}
  .brand{position:absolute;left:0;top:2162px;width:1200px;height:355px;background:var(--white)}
  .brand__mark{position:absolute;left:68px;top:90px;width:150px;height:150px;border-radius:50%;background:var(--sky)}
  .brand__name{position:absolute;left:300px;top:36px;font-size:120px;line-height:140px;color:var(--ink);white-space:nowrap}
  .brand__tag{position:absolute;left:396px;top:192px;font-size:50px;line-height:60px;letter-spacing:14px;color:var(--ink);white-space:nowrap}
  .brand__web{position:absolute;left:300px;top:282px;font-size:34px;line-height:42px;color:var(--navy);white-space:nowrap}
</style>
</head>
<body>
<main class="flyer">
  <div class="pool-photo" role="img" aria-label="Photo of a kidney-shaped backyard swimming pool with blue water and paved stone surround"></div>
  <div class="top-rule"></div>
  <h1 class="headline">For All Your<br>Cleaning &amp; Maintenance<br>Needs</h1>
  <p class="reassure">Never worry about your pool again</p>

  <div class="water"></div>
  <svg class="wave" viewBox="0 0 1200 240" preserveAspectRatio="none" aria-hidden="true">
    <defs>
      <linearGradient id="waveFill" x1="0" y1="0" x2="0" y2="1">
        <stop offset="0" stop-color="#e9f6fd"/>
        <stop offset="1" stop-color="#2f8fdc"/>
      </linearGradient>
    </defs>
    <path d="M0 60 C200 20 360 110 600 80 C820 52 980 20 1200 40 L1200 240 L0 240 Z" fill="url(#waveFill)"/>
    <path d="M0 120 C220 70 420 150 640 120 C860 90 1000 70 1200 95 L1200 240 L0 240 Z" fill="#3a9ae2" opacity=".85"/>
    <path d="M0 118 C220 68 420 148 640 118 C860 88 1000 68 1200 93" fill="none" stroke="#ffffff" stroke-width="6" opacity=".9"/>
  </svg>
  <div class="droplets" role="img" aria-label="Water droplets splashing beneath the wave"></div>

  <ul class="services">
    <li>Pool Resurfacing</li>
    <li>Electronic Leak Detection &amp; General Repairs</li>
    <li>2-pack Epoxy or Chlorinated Rubber</li>
    <li>Sand Changes &amp; Replacement of Filters</li>
    <li>Pool accessories &amp; Chemicals</li>
    <li>Installation of Pumps &amp; Piping</li>
  </ul>

  <div class="offer-band"></div>
  <div class="contact-panel"></div>
  <p class="frequency">One-off, Weekly, Fortnightly<br>or Monthly Services Available</p>

  <div class="price-badge">
    <div class="price-badge__inner">
      <span class="price-badge__label">Monthly</span>
      <span class="price-badge__sub">Pool Service is</span>
      <span class="price-badge__amount">$67.00</span>
      <span class="price-badge__note">Plus Chemicals</span>
    </div>
  </div>

  <p class="call-to-action">For Prompt Reliable Service<br>Call Today</p>
  <p class="phones">4821 5730<span class="sep">|</span>4826 9150<br>0491 570 318</p>

  <div class="footer-rule"></div>
  <footer class="brand">
    <span class="brand__mark"></span>
    <span class="brand__name">Bright Ripple</span>
    <span class="brand__tag">POOL CARE</span>
    <span class="brand__web">www.brightripplepoolcare.com.au</span>
  </footer>
</main>
</body>
</html>
```